Vale Crest Motors Business Card

Would like a cutting edge / high end Automotive Business card design. Please see current card which is old and dated. Would like to maintain the Vale Crest Motors logo and same information (address, website, etc).

See our website for the look and feel of what we offer - www.valecrestmotors.example

Target Market(s)

Upper class car buyers

Contact Information for Business Card

Modern high end business card design

Requirements
Nice to have
• Carbon Fiber look background

```html
<!DOCTYPE html>
<html lang="en">
<head>
<meta charset="utf-8">
<title>Vale Crest Motors – Business Card</title>
<link href="https://fonts.googleapis.com/css2?family=Lato:wght@400;700&display=swap" rel="stylesheet">
<style>
  :root {
    --backdrop: #1c1c1e;
    --card: #0b0b0c;
    --card-edge: #151517;
    --ink: #f2f2f2;
    --ink-soft: #bdbdbd;
    --silver: #cfcfd2;
    --rule: #6a6a6e;
  }
  * { margin: 0; padding: 0; box-sizing: border-box; }
  html, body {
    width: 1200px; height: 900px; overflow: hidden;
    background: var(--backdrop);
    font-family: 'Lato', sans-serif;
  }
  .sheet {
    width: 1200px; height: 900px;
    display: flex; flex-direction: column;
    align-items: center; justify-content: center; gap: 40px;
  }
  .card {
    position: relative;
    width: 700px; height: 400px;
    background: radial-gradient(ellipse at 40% 30%, var(--card-edge), var(--card) 70%);
    border-radius: 4px;
    color: var(--ink);
  }
  .wordmark {
    position: absolute; left: 0; right: 0;
    text-align: center;
  }
  .wordmark__name {
    display: inline-block;
    font-weight: 400;
    font-size: 46px;
    letter-spacing: 6px;
    text-transform: uppercase;
    padding-bottom: 14px;
    border-bottom: 1px solid var(--rule);
  }
  .card--front .wordmark { top: 58px; }
  .card--back .wordmark { top: 160px; }
  .card--back .wordmark__name { color: var(--silver); }

  .holder {
    position: absolute; left: 150px; top: 232px;
    width: 190px; text-align: right;
  }
  .holder__name { font-weight: 700; font-size: 22px; letter-spacing: 0.5px; }
  .holder__role { font-size: 17px; color: var(--ink-soft); margin-top: 2px; }

  .divider {
    position: absolute; left: 362px; top: 182px;
    width: 1px; height: 110px; background: var(--rule);
  }
  .contacts {
    position: absolute; left: 382px; top: 182px;
    list-style: none; font-size: 18px; line-height: 28px;
  }
  .contacts li { display: flex; align-items: center; gap: 9px; }
  .contacts svg { width: 15px; height: 15px; fill: var(--ink); flex: none; }

  .address {
    position: absolute; left: 0; right: 0; top: 330px;
    text-align: center; font-size: 18px;
  }
</style>
</head>
<body>
<main class="sheet">
  <section class="card card--front">
    <div class="wordmark"><span class="wordmark__name">Vale Crest Motors</span></div>

    <div class="holder">
      <p class="holder__name">ADRIAN HALE</p>
      <p class="holder__role">Managing Director</p>
    </div>

    <div class="divider"></div>

    <ul class="contacts">
      <li>
        <svg viewBox="0 0 16 16" aria-hidden="true"><path d="M3.6 1.5l2.4 2.6-1.4 1.8c.9 2 2.5 3.6 4.5 4.5l1.8-1.4 2.6 2.4-1.6 2.1C6.6 13.3 2.7 9.4 1.5 3.1z"/></svg>
        077-555 010 274
      </li>
      <li>
        <svg viewBox="0 0 16 16" aria-hidden="true"><path d="M1 3h14v10H1z M2.2 4.2v.3L8 8.6l5.8-4.1v-.3z" fill-rule="evenodd"/></svg>
        info@valecrestmotors.example
      </li>
      <li>
        <svg viewBox="0 0 16 16" aria-hidden="true"><circle cx="8" cy="8" r="7"/></svg>
        www.valecrestmotors.example
      </li>
    </ul>

    <p class="address">88, Harbour Row, 20917, Westmere</p>
  </section>

  <section class="card card--back">
    <div class="wordmark"><span class="wordmark__name">Vale Crest Motors</span></div>
  </section>
</main>
</body>
</html>
```